NZ First of it's kind solutions directory and marketplace for busy Mums needs a business card design

We need a business card design for our new nationwide business in NZ (long term plans to go global). We provide solutions to the everyday challenges that busy Mums face by connecting them with quality communities and suppliers of carefully selected, relevant products and services. We sell direct via our online marketplace. The final design should communicate our values of inclusivity, quality and smart solutions. Colours should incorporate our logo colour palette of #477077 and #6ba8b2. Our website is at https://www.brightnestly.com

Target Market(s)

busy Mums, Age 28 – 50, female, income over $100K, location main centres NZ primarily but NZ wide. Is likely juggling work or career with a young family. Probably had hobbies which have fallen by the wayside.
-Wants to succeed in her chosen career without compromising on family life
-to successfully juggle her career without feeling like she is compromising her children
- Is time poor, something always has to give and it’s generally her health (she’ll stay up late, get stressed)
- probably ex corporate or professional career. Has discretional income

Industry/Entity Type

Business

Contact Information for Business Card

Lena Hartwell, Founder, BrightNestly.com (Strapline Click; Connect; Done), 48 Kowhai Terrace, Ferndale, Auckland 1071, New Zealand. Mob: 021 437 518 Ph: +64 (0)9 581 4706

Font styles to use
Other font styles liked:
• Raleway, and/or Architects Daughter

Colors
00a990
33b8a4
86cfc6
cfeae6

Requirements
Must have
• the above details, streamline. the logo and colours associated with those logos
Should not have
• foil or metallic colours

```html
<!DOCTYPE html>
<html lang="en">
<head>
<meta charset="utf-8">
<title>BrightNestly business card</title>
<link rel="stylesheet" href="https://fonts.googleapis.com/css2?family=Raleway:wght@400;500;600;700&display=swap">
<style>
  :root {
    --page-bg: #d8d3cb;
    --card-light: #f1f4f3;
    --card-mist: #dde5e5;
    --brand-dark: #2f5960;
    --brand-teal: #477077;
    --brand-aqua: #6ba8b2;
    --band-deep: #2b474c;
    --band-mid: #4f8189;
    --band-soft: #5f929a;
    --ink-light: #e8efef;
    --ink-muted: #cfdcdc;
    --social: #2d4a4f;
  }
  * { margin: 0; padding: 0; box-sizing: border-box; }
  html, body {
    width: 1200px; height: 970px; overflow: hidden;
    background: var(--page-bg);
    font-family: "Raleway", sans-serif;
  }
  .card {
    position: absolute; left: 80px; top: 190px;
    width: 1040px; height: 590px;
    border-radius: 24px; overflow: hidden;
    background: linear-gradient(160deg, var(--card-light) 0%, var(--card-mist) 100%);
    box-shadow: 0 10px 30px rgba(0,0,0,0.18);
  }
  .card__band { position: absolute; left: 0; top: 0; width: 1040px; height: 590px; }
  .brand { position: absolute; left: 52px; top: 92px; display: flex; align-items: center; gap: 22px; }
  .brand__dot { width: 62px; height: 62px; border-radius: 50%; background: var(--brand-teal); }
  .brand__name { font-size: 70px; font-weight: 700; color: var(--brand-dark); letter-spacing: -1.5px; line-height: 1; }
  .social { position: absolute; left: 738px; top: 50px; display: flex; gap: 6px; }
  .social__item { width: 44px; height: 44px; border-radius: 50%; background: var(--social); }
  .tagline { position: absolute; left: 50px; top: 262px; font-size: 25px; font-weight: 500; color: var(--brand-teal); white-space: nowrap; }
  .person { position: absolute; left: 50px; top: 352px; color: var(--ink-light); }
  .person__name { font-size: 30px; font-weight: 700; letter-spacing: -0.5px; line-height: 1.05; }
  .person__role { font-size: 25px; font-weight: 400; line-height: 1.1; color: var(--ink-muted); }
  .phones { position: absolute; left: 50px; top: 472px; list-style: none; color: var(--ink-muted); font-size: 25px; }
  .phones__item { display: flex; align-items: center; gap: 10px; height: 34px; }
  .phones__icon { width: 24px; height: 24px; }
  .address { position: absolute; left: 698px; top: 405px; font-style: normal; font-size: 25px; line-height: 32px; color: var(--ink-muted); white-space: nowrap; }
  .website { position: absolute; right: 60px; top: 537px; font-size: 25px; color: var(--ink-muted); white-space: nowrap; }
</style>
</head>
<body>
  <article class="card">
    <svg class="card__band" viewBox="0 0 1040 590" aria-hidden="true">
      <defs>
        <linearGradient id="bandMid" x1="0" y1="0" x2="1" y2="1">
          <stop offset="0" stop-color="#5f929a"/>
          <stop offset="1" stop-color="#4f8189"/>
        </linearGradient>
      </defs>
      <rect x="0" y="335" width="1040" height="255" fill="#2b474c"/>
      <path d="M0 442 H405 C438 442 432 397 468 397 H1040 V522 H642 C610 522 616 590 584 590 H0 Z" fill="url(#bandMid)"/>
    </svg>

    <div class="brand">
      <span class="brand__dot"></span>
      <span class="brand__name">BrightNestly</span>
    </div>

    <div class="social" aria-label="Social media links">
      <span class="social__item"></span>
      <span class="social__item"></span>
      <span class="social__item"></span>
      <span class="social__item"></span>
      <span class="social__item"></span>
    </div>

    <p class="tagline">Everyday Help for Busy Mums. Find, Choose, Relax.</p>

    <div class="person">
      <p class="person__name">Lena Hartwell</p>
      <p class="person__role">Founder</p>
    </div>

    <ul class="phones">
      <li class="phones__item">
        <svg class="phones__icon" viewBox="0 0 24 24" aria-hidden="true">
          <circle cx="12" cy="12" r="11" fill="none" stroke="currentColor" stroke-width="1.5"/>
          <rect x="8.5" y="5.5" width="7" height="13" rx="1.2" fill="none" stroke="currentColor" stroke-width="1.5"/>
        </svg>
        <span>021 437 518</span>
      </li>
      <li class="phones__item">
        <svg class="phones__icon" viewBox="0 0 24 24" aria-hidden="true">
          <circle cx="12" cy="12" r="11" fill="none" stroke="currentColor" stroke-width="1.5"/>
          <path d="M6 10 Q12 5 18 10 L16.5 11.5 L14.5 10 L9.5 10 L7.5 11.5 Z M8 12 H16 L17 17 H7 Z" fill="currentColor"/>
        </svg>
        <span>+64 (0)9 581 4706</span>
      </li>
    </ul>

    <address class="address">
      48 Kowhai Terrace,<br>
      Ferndale, Auckland 1071<br>
      New Zealand
    </address>

    <p class="website">www.brightnestly.com</p>
  </article>
</body>
</html>
```